Sophrologist needs a cool signage at door entrance

I need signage for dr in sophrology based in Belgium (french speaking). The signed should capture the name the "Mireille Vantoorn" - "Naturopathe-Sophrologue-Reiki" and a catchphrase = (Serene way of living)
« Fais du bien à ton corps, pour que ton âme ait envie d’y rester »
Requirements
Must have
- Hey,
Thats the instagram account for some inspiration www.instagram.com/mireille_serene_wellbeing
Light colors, green, blue
Serene way of living
Size is 45cm wide on 30 cm high
The signage will be placed in front off woof pannel

```html
<!DOCTYPE html>
<html lang="fr">
<head>
<meta charset="utf-8">
<title>Mireille Vantoorn – Serene way of living</title>
<link rel="stylesheet" href="https://fonts.googleapis.com/css2?family=Montserrat:wght@200;400;700;800;900&display=swap">
<style>
  :root {
    --sky-top: #ffffff;
    --sky-mid: #e6f2fa;
    --sky-low: #cfe6f4;
    --lavender: #d9d8f0;
    --leaf-green: #bdd46f;
    --band-blue: #9ccbe7;
    --title-blue: #3a9fcc;
    --dash-grey: #6d7b85;
    --white: #ffffff;
  }
  html, body {
    margin: 0;
    padding: 0;
    overflow: hidden;
    background: var(--white);
  }
  .sign {
    position: relative;
    width: 1200px;
    height: 800px;
    overflow: hidden;
    font-family: 'Montserrat', Arial, sans-serif;
  }
  .sign__canvas {
    display: block;
    width: 1200px;
    height: 800px;
  }
  .name-first { font-weight: 800; fill: var(--white); }
  .name-last { font-weight: 200; fill: var(--white); }
  .service { font-weight: 700; fill: var(--title-blue); }
  .service-dash { font-weight: 400; fill: var(--dash-grey); }
  .tagline { font-weight: 800; fill: var(--white); }
</style>
</head>
<body>
<main class="sign">
  <svg class="sign__canvas" viewBox="0 0 1200 800" xmlns="http://www.w3.org/2000/svg">
    <defs>
      <linearGradient id="sky" x1="0" y1="0" x2="0" y2="1">
        <stop offset="0" stop-color="var(--sky-top)"/>
        <stop offset="0.35" stop-color="var(--sky-mid)"/>
        <stop offset="1" stop-color="var(--sky-low)"/>
      </linearGradient>
      <linearGradient id="haze" x1="0" y1="1" x2="1" y2="0">
        <stop offset="0" stop-color="var(--lavender)" stop-opacity="0.7"/>
        <stop offset="0.5" stop-color="var(--sky-low)" stop-opacity="0.2"/>
        <stop offset="1" stop-color="var(--sky-top)" stop-opacity="0"/>
      </linearGradient>
    </defs>

    <g class="backdrop" role="img" aria-label="Soft pale blue sky background with faint white butterflies and floral swirls">
      <rect width="1200" height="800" fill="url(#sky)"/>
      <rect y="560" width="1200" height="240" fill="url(#haze)"/>
    </g>

    <g class="name-block">
      <rect class="name-panel" x="0" y="191" width="722" height="268" fill="var(--leaf-green)"/>
      <text class="name-first" x="141" y="315" font-size="108">Mireille</text>
      <text class="name-last" x="103" y="418" font-size="104">Vantoorn</text>
    </g>

    <g class="services" font-size="50">
      <text class="service-dash" x="774" y="288">-</text>
      <text class="service" x="818" y="290">Naturopathe</text>
      <text class="service-dash" x="774" y="346">-</text>
      <text class="service" x="818" y="348">Sophrologue</text>
      <text class="service-dash" x="774" y="402">-</text>
      <text class="service" x="818" y="404">Reiki</text>
    </g>

    <g class="tagline-band">
      <rect x="0" y="459" width="722" height="5" fill="var(--white)"/>
      <rect x="0" y="464" width="1200" height="145" fill="var(--band-blue)" fill-opacity="0.95"/>
      <text class="tagline" x="75" y="564" font-size="63" textLength="1053" lengthAdjust="spacing">SERENE WAY OF LIVING</text>
    </g>
  </svg>
</main>
</body>
</html>
```